My dynamic new collection of short plays needs an eye catching web-based ad!

I am buying ad space on a theater magazine's website with these specs for a new book. The ad will run for a few months. I have the book cover - which will be the main image, but need the ad designed with quotes and the publisher's logo. Here are the specs:
230 pixels wide x 250 pixels high
72 dpi

Target Market(s)

Theater artists and theater educators

Industry/Entity Type

Theater / Education

Font styles to use
Sans Serif
Other font styles liked:
• Please use fonts that match the book cover. I'm including an ad that is currently on the website where I will be advertising. It is not the size that I'm going for, but it contains the elements that I want. I'm also including an image of the logo of the publisher, and I have other versions of this logo (other formats / larger size) that I can deliver if needed.

Requirements
Must have
• Simple compelling image with a quote from the book and a link to the publisher website. A compelling quote (or two) from the book jacket. The name and logo of the publisher.
Nice to have
• Some eye catching color to compliment the beautiful cover design
Should not have
• Too much busy-ness in the image or the presentation.

```html
<!DOCTYPE html>
<html lang="en">
<head>
<meta charset="utf-8">
<title>A Few Short Plays to Mend the World — Book Ad</title>
<link href="https://fonts.googleapis.com/css2?family=Montserrat:wght@500;600;700;800&display=swap" rel="stylesheet">
<style>
  :root {
    --ink-blue: #0a2396;
    --ink-black: #111111;
    --ink-grey: #3a3a3a;
    --rule: #333333;
    --panel: #eef9fc;
    --panel-glow: #ffffff;
    --cover-deep: #1f3fae;
    --cover-mid: #3a78d6;
    --cover-light: #7fc8ec;
    --spine: #1c2f9c;
    --page-edge: #e8e8ee;
    --button-top: #4258c6;
    --button-bottom: #0a2396;
    --white: #ffffff;
  }
  * { margin: 0; padding: 0; box-sizing: border-box; }
  html, body {
    width: 1200px;
    height: 1200px;
    overflow: hidden;
  }
  body {
    font-family: "Montserrat", sans-serif;
    background: radial-gradient(circle at 50% 48%, var(--panel-glow) 0%, var(--panel) 72%);
  }
  .ad {
    position: relative;
    width: 1200px;
    height: 1200px;
  }
  .headline {
    position: absolute;
    top: 50px;
    left: 0;
    width: 100%;
    text-align: center;
    color: var(--ink-blue);
    font-weight: 800;
    font-size: 78px;
    line-height: 94px;
    letter-spacing: 0.5px;
  }
  .book {
    position: absolute;
    top: 272px;
    left: 420px;
    width: 360px;
    height: 520px;
    display: block;
    filter: drop-shadow(0 14px 18px rgba(20, 40, 90, 0.18));
  }
  .author {
    position: absolute;
    top: 826px;
    left: 0;
    width: 100%;
    text-align: center;
    font-weight: 800;
    font-size: 30px;
    letter-spacing: 14px;
    padding-left: 14px;
    color: var(--ink-black);
  }
  .quote {
    position: absolute;
    top: 880px;
    left: 260px;
    width: 680px;
  }
  .quote-rule {
    display: flex;
    align-items: center;
    gap: 14px;
    height: 24px;
  }
  .quote-rule::before,
  .quote-rule::after {
    content: "";
    flex: 1;
    height: 1.5px;
    background: var(--rule);
  }
  .quote-mark {
    color: var(--ink-blue);
    font-weight: 800;
    font-size: 40px;
    line-height: 1;
    height: 24px;
    overflow: hidden;
  }
  .quote-mark.open { padding-top: 5px; }
  .quote-mark.close { padding-top: 3px; }
  .quote-text {
    text-align: center;
    font-weight: 500;
    font-size: 21.5px;
    line-height: 33px;
    color: var(--ink-black);
    padding: 4px 0 6px;
    white-space: nowrap;
  }
  .attribution {
    position: absolute;
    top: 1034px;
    left: 0;
    width: 100%;
    text-align: center;
    line-height: 26px;
  }
  .attribution-name {
    display: block;
    color: var(--ink-blue);
    font-weight: 700;
    font-size: 18px;
  }
  .attribution-role {
    display: block;
    color: var(--ink-black);
    font-weight: 500;
    font-size: 17px;
  }
  .publisher {
    position: absolute;
    top: 866px;
    left: 45px;
    width: 180px;
    display: flex;
    flex-direction: column;
    align-items: center;
    gap: 14px;
  }
  .publisher-dot {
    width: 120px;
    height: 120px;
    border-radius: 50%;
    background: var(--ink-grey);
  }
  .publisher-name {
    color: var(--ink-grey);
    font-weight: 500;
    font-size: 14px;
    letter-spacing: 1.5px;
    text-align: center;
    line-height: 20px;
    text-transform: uppercase;
  }
  .publisher-name .imprint {
    letter-spacing: 6px;
    font-size: 12px;
  }
  .buy-button {
    position: absolute;
    top: 872px;
    left: 985px;
    width: 156px;
    height: 156px;
    border-radius: 50%;
    background: linear-gradient(160deg, var(--button-top) 0%, var(--button-bottom) 65%);
    color: var(--white);
    font-weight: 800;
    font-size: 36px;
    line-height: 40px;
    text-align: center;
    text-decoration: none;
    display: flex;
    align-items: center;
    justify-content: center;
  }
</style>
</head>
<body>
  <main class="ad">
    <h1 class="headline">A FEW SHORT PLAYS<br>TO MEND THE WORLD</h1>

    <svg class="book" viewBox="0 0 360 520" role="img" aria-label="Hardcover book showing a colourful low-poly portrait of the author on a blue cover with the title A Few Short Plays to Mend the World">
      <defs>
        <radialGradient id="coverFill" cx="0.55" cy="0.45" r="0.75">
          <stop offset="0" stop-color="var(--cover-light)"/>
          <stop offset="0.55" stop-color="var(--cover-mid)"/>
          <stop offset="1" stop-color="var(--cover-deep)"/>
        </radialGradient>
      </defs>
      <rect x="316" y="12" width="34" height="492" fill="var(--spine)"/>
      <rect x="316" y="8" width="26" height="500" fill="var(--page-edge)"/>
      <rect x="10" y="22" width="310" height="490" fill="url(#coverFill)"/>
    </svg>

    <p class="author">MARCUS DELANEY</p>

    <blockquote class="quote">
      <div class="quote-rule"><span class="quote-mark open">&ldquo;</span></div>
      <p class="quote-text">Marcus provokes us to look more carefully at systems<br>of race and power and our participation in them<br>in ways that linger long after the blackout.</p>
      <div class="quote-rule"><span class="quote-mark close">&rdquo;</span></div>
    </blockquote>

    <p class="attribution">
      <span class="attribution-name">Dana Whitfield</span>
      <span class="attribution-role">Artistic Director, Brightline Stage</span>
    </p>

    <div class="publisher">
      <span class="publisher-dot"></span>
      <span class="publisher-name">Grinning Otter<br><span class="imprint">Press</span></span>
    </div>

    <a class="buy-button" href="#">Buy<br>Now</a>
  </main>
</body>
</html>
```